Kovrix - consultancy website

I need a new design for my webpage/presence [to be functioning with Wordpress - I have a programmer to set it up but not the design idea].
My company is Kovrix - a consultancy firm focused on growth management for Swedish SME's primarily;. We call it Leadership add-on for firms on the rise, kind of a doctor helping small become big. Contentwise, its a simple frontpage + 3-4 subpages with content re company/myself/focus etc. The new site should communicate a fresh, trustworthy take yet simple and functional on all devices [i.e. think UI compatible for mobile/tablet]. Current building parts/form elements are
a) existing logo and text elements
b) existing pictures
c) the yellowish color
colours and new ideas on pictures/positioning are welcome. I prefer a 'full width page' solution with centralised text elements but that's all up to you to suggest. Current site is a quickfix made by myself - now I'm moving it to a new platform so want to take the opportunity to make it
Nothing superspecial as it is a 2-man show; on the other hand I still want to have a modern & fresh reflection of my brand in digital environments. Help me out!
www.kovrix-demo.se
Best
Lotta Bergqvalm

```html
<!DOCTYPE html>
<html lang="en">
<head>
<meta charset="utf-8">
<title>Kovrix – Leadership add-on for firms on the rise</title>
<link href="https://fonts.googleapis.com/css2?family=Open+Sans:wght@300;400;600;700;800&display=swap" rel="stylesheet">
<style>
  :root{
    --ink:#3c4048;
    --ink-deep:#353940;
    --accent:#f4a322;
    --paper:#ffffff;
    --mist:#f1f2f4;
    --line:#c9cbcf;
    --muted:#8a8d93;
    --heading:#6d7077;
  }
  *{box-sizing:border-box;margin:0;padding:0}
  html,body{width:681px;height:1200px;overflow:hidden}
  body{font-family:"Open Sans",Arial,sans-serif;background:var(--paper);position:relative;color:var(--ink)}
  section,header,footer{position:absolute;left:0;width:681px}

  .site-header{top:0;height:64px;background:var(--paper);border-top:3px solid var(--accent)}
  .brand{position:absolute;left:93px;top:14px;font-weight:700;font-size:24px;color:var(--ink)}
  .main-nav{position:absolute;right:40px;top:24px;display:flex;gap:14px}
  .main-nav a{font-size:10px;font-weight:700;color:var(--ink);text-decoration:none;letter-spacing:.3px}

  .hero{top:64px;height:266px;background:var(--ink)}
  .hero-title{position:absolute;left:93px;top:34px;font-size:35px;font-weight:800;color:var(--accent);letter-spacing:.5px}
  .hero-text{position:absolute;left:93px;top:88px;width:250px;font-size:8px;line-height:1.45;color:#fff}
  .signup{position:absolute;display:flex;gap:10px}
  .hero .signup{left:93px;top:132px}
  .field{height:22px;background:#4a4e56;color:#a3a6ac;font-size:7px;padding:0 10px;display:flex;align-items:center}
  .signup .field{width:178px}
  .btn{height:22px;width:52px;background:var(--accent);color:#fff;font-size:7px;font-weight:700;display:flex;align-items:center;justify-content:center;border-radius:2px}
  .social{position:absolute;left:93px;top:172px;display:flex;gap:8px}
  .social span{width:20px;height:20px;border:1.5px solid var(--accent);border-radius:50%}
  .hero-portrait{position:absolute;left:505px;top:16px;width:150px;height:250px;background:linear-gradient(180deg,#5a5e66,#2c2f35)}

  .services{top:330px;height:278px;background:var(--paper)}
  .section-title{position:absolute;left:0;width:100%;text-align:center;font-weight:300;color:var(--heading)}
  .services .section-title{top:28px;font-size:27px}
  .service-tree{position:absolute;left:0;top:0}
  .service{position:absolute;top:160px;width:160px;text-align:center}
  .service h3{font-size:13px;font-weight:700;color:var(--ink);margin-bottom:8px}
  .service p{font-size:7px;line-height:1.5;color:var(--muted)}

  .newsletter{top:608px;height:164px;background:var(--ink)}
  .newsletter-title{position:absolute;left:93px;top:26px;font-size:17px;font-weight:800;color:var(--accent)}
  .newsletter-text{position:absolute;left:93px;top:54px;width:300px;font-size:8px;line-height:1.45;color:#fff}
  .newsletter .signup{left:93px;top:104px}
  .newsletter-photo{position:absolute;left:477px;top:0;width:204px;height:164px;background:radial-gradient(circle at 50% 45%,#c9a27a,#8a6447 70%,#6e4e36)}

  .contact{top:772px;height:310px;background:var(--paper)}
  .contact .section-title{top:26px;font-size:25px}
  .contact-row{position:absolute;left:93px;top:82px;display:flex;gap:13px}
  .contact .field{background:var(--mist);color:#9a9ca1;width:157px;height:24px}
  .contact .message{position:absolute;left:93px;top:118px;width:497px;height:132px;background:var(--mist);font-size:7px;color:#9a9ca1;padding:8px 10px}
  .contact .btn{position:absolute;left:315px;top:263px}

  .site-footer{top:1082px;height:118px;background:var(--ink-deep)}
  .footer-brand{position:absolute;left:93px;top:30px;font-size:22px;font-weight:700;color:#fff}
  .footer-note{position:absolute;left:93px;top:62px;font-size:7px;color:var(--accent)}
  .footer-social{position:absolute;left:530px;top:44px;display:flex;gap:7px}
  .footer-social span{width:16px;height:16px;border:1.5px solid var(--accent);border-radius:50%}
</style>
</head>
<body>
  <header class="site-header">
    <div class="brand">Kovrix.</div>
    <nav class="main-nav"><a href="#">HOME</a><a href="#">SERVICES</a><a href="#">ABOUT</a><a href="#">CONTACT</a></nav>
  </header>

  <section class="hero">
    <h1 class="hero-title">WE DELIVER</h1>
    <p class="hero-text">We guide growing companies through change with clear structure, steady leadership and practical tools that help small teams scale with confidence and calm.</p>
    <div class="signup"><div class="field">enter your email</div><div class="btn">SUBMIT</div></div>
    <div class="social"><span></span><span></span><span></span></div>
    <div class="hero-portrait" role="img" aria-label="Portrait photo of the consultant, arms crossed"></div>
  </section>

  <section class="services">
    <h2 class="section-title">Service</h2>
    <svg class="service-tree" width="681" height="160" viewBox="0 0 681 160">
      <g stroke="#c9cbcf" stroke-width="1.2" fill="none">
        <line x1="340" y1="72" x2="340" y2="95"/>
        <line x1="170" y1="95" x2="510" y2="95"/>
        <line x1="170" y1="95" x2="170" y2="110"/>
        <line x1="340" y1="95" x2="340" y2="110"/>
        <line x1="510" y1="95" x2="510" y2="110"/>
      </g>
      <g fill="#c9cbcf"><circle cx="340" cy="72" r="2.5"/><circle cx="170" cy="110" r="2.5"/><circle cx="340" cy="110" r="2.5"/><circle cx="510" cy="110" r="2.5"/></g>
      <g stroke="#f4a322" stroke-width="2.2" fill="none" stroke-linecap="round">
        <circle cx="170" cy="138" r="11"/><circle cx="170" cy="138" r="4.5"/>
        <line x1="162" y1="130" x2="167" y2="135"/><line x1="178" y1="130" x2="173" y2="135"/>
        <line x1="162" y1="146" x2="167" y2="141"/><line x1="178" y1="146" x2="173" y2="141"/>
        <path d="M332 126h11l6 6v18h-17z"/><path d="M343 126v6h6"/>
        <line x1="336" y1="139" x2="345" y2="139"/><line x1="336" y1="144" x2="345" y2="144"/>
        <path d="M510 126a8 8 0 0 0-5 14.5v3.5h10v-3.5a8 8 0 0 0-5-14.5z"/>
        <line x1="506" y1="148" x2="514" y2="148"/>
      </g>
    </svg>
    <div class="service" style="left:90px"><h3>What We do</h3><p>Hands-on leadership support for owners who need structure, routines and a clear plan for the next stage.</p></div>
    <div class="service" style="left:260px"><h3>What We are</h3><p>A small senior team with long experience from growth firms, boards and management roles in Sweden.</p></div>
    <div class="service" style="left:430px"><h3>Why We</h3><p>Growth brings new demands. We help you meet them early, keep focus and build a firm that lasts.</p></div>
  </section>

  <section class="newsletter">
    <h2 class="newsletter-title">SUBSCRIBE TO OUR NEWSLETTER</h2>
    <p class="newsletter-text">Short notes on leadership, growth and management for small firms, sent once a month straight to your inbox.</p>
    <div class="signup"><div class="field">enter your email</div><div class="btn">SUBMIT</div></div>
    <div class="newsletter-photo" role="img" aria-label="Overhead photo of a wooden table with cups and small objects"></div>
  </section>

  <section class="contact">
    <h2 class="section-title">Contact</h2>
    <div class="contact-row">
      <div class="field">enter your name</div>
      <div class="field">enter your email</div>
      <div class="field">enter your website</div>
    </div>
    <div class="message">Message...</div>
    <div class="btn">SUBMIT</div>
  </section>

  <footer class="site-footer">
    <div class="footer-brand">Kovrix.</div>
    <div class="footer-note">Growth partner · © 2024 · All rights reserved</div>
    <div class="footer-social"><span></span><span></span><span></span></div>
  </footer>
</body>
</html>
```